■依頼の目的/概要
ベストセラー作家が送る最新作の表紙を飾りませんか?
Borelo QuillのBWSの電子書籍表紙デザインをお願いします。

■本の内容
*タイトル:
うつむく朝に灯すひと匙の言葉

というタイトルの表紙デザインの発注になります。

■デザイン要望

要望1つ目
作家名は後でお伝えします。作家名もどこかに挿入いただきたいです。よろしくお願いします。
提出の際は ○○著という形でご提出よろしくお願いします。

要望2つ目
ウェルネスバランスコーチ検定資格保持者

とどこかに入れてください。

要望3つ目
累計Borelo 1位〇冠
(現在、59冠までいっています。今後、出版が控えている作品があります。
そのため、その最終冠数を入れて頂きたいです。)

とどこかに入れてください。

また、出来上がったデザインを作家グループの中で投票にかけて、
一番投票得票数の多かったものを表紙デザインとして選ばせていただきたいと考えております。
もしかしたら、その中で、何か修正依頼など来るかもしれませんが、
それも含めて、ご対応していただける方よろしくお願いします。

また、最終、選考後、
累計Borelo 1位〇〇冠   と記載された表紙と、
累計Borelo 1位〇〇冠   と記載されない表紙の
2表紙の納品をよろしくお願いします。他の部分の表紙のデザイン変更は不要です。
(これは、最終選ばれたデザイナーさんのみご対応で大丈夫です。)

お手数をおかけしますが、よろしくお願いします。

1部内容の抜粋を記載します。

データサイズですが、推奨サイズでJPEGファイルでご納品下さい、よろしくお願いします。
(推奨サイズは2560×1600pxです。)
その他何かご不明な点がございましたら、お気軽にご質問下さい。
よろしくお願いいたします。
変更点がでてきました。

累計Borelo 1位〇〇冠→累計Borelo 1位65冠
と決定しました。最終、この数字でご納品ください。

もうすでに提出済みの方に関しましては、当選後のご対応で大丈夫です。
お手数をおかけしますが、ご対応なにとぞよろしくお願いいたします。
皆様、たくさんのご応募まことにありがとうございました。
コンペというとても厳しい条件にも関わらず、挑戦いただいたことに
大変大変感謝しております。
ご提案されましたすべての作品、デザイナー様のご経歴、作成への思い入れ、
すべてを拝見させていただきました。
これから、作家グループへ全体回覧のメールを致します。
作家グループの皆様の投票結果までお待ちください(場合により結果
公表まで1週間から10日ぐらいかかる場合もあると思われます)。
また、この度、いろいろな作品に触れさせていただきましたこと本当に
本当に感謝いたします。
皆さまのご努力、精進そしてそのチャレンジに大変感謝と尊敬を感じております。
ご経歴やデザイナー様の名前などすべて伏せて、作品のみの提示にて
小説家作家グループに提案させていただきたいと思っております。
ただ、今回の表紙に関しましては、どうしても1名しか選べない状況がございますこと
また、総選挙による投票にて決定致しますこと、ご理解何卒よろしくお願い申しあげます。
また、もしも、今回当選に至らないことがありましても、
今後も私自身は作家生活を継続予定ですので、
(今回は作品の表紙に合わないことがあっても)作風の気に入ったデザイナー様には
個人的にお話を相談させていただく場合もあると思っております。
また、別の作品の表紙を飾っていただく可能性もあるかと思っております。
この度は誠に誠にありがとうございました。
表紙ですが、最終選考決定いたしました。
当選された方には個別に連絡をさせていただきました。

皆様からのご提案、そして、そのチャレンジに敬意と感謝をしております。
私はこれからも作家活動を継続致しますので、また、ご一緒にお仕事をさせていただき
表紙を飾っていただく機会もあるかと思います。
その際はなにとぞよろしくお願いもうしあげます。
自分のためだけでなく、ベストセラーを取り続けることで、素晴らしい表紙を飾れるチャンスをこれからも作りたいと思い、また、精進していきたいと思います。
この度はまことにありがとうございました。

「目が惹きつけられました」とか
これから上を向いて、光を見て行こうとする視線と深く、それでいて爽やかなブルーのタッチがとても印象的で綺麗‼️
など目が離せない、というようなコメントを多くいただきました。
ご提出誠にありがとうございます。

コンペについてはとても厳しい条件にも関わらず挑戦していただき、
本当に一つのタイトルに対する皆様の創造力について驚きや才能についてをいつも
感じています。
そして、そのチャレンジする姿勢にいつもエネルギーをいただき、
私自身もこれからも、いろいろなことに挑戦する姿勢を続けていきたいな、
と感じております。
表紙を飾っていただく機会もあるかと思います。
その際はなにとぞよろしくお願いもうしあげます。この度はありがとうございました。

```html
<!DOCTYPE html>
<html lang="ja">
<head>
<meta charset="UTF-8">
<title>うつむく朝に灯すひと匙の言葉</title>
<link rel="stylesheet" href="https://fonts.googleapis.com/css2?family=Noto+Sans+JP:wght@500;700;900&family=M+PLUS+Rounded+1c:wght@700;800&display=swap">
<style>
  :root {
    --ink: #1d1d1f;
    --teal: #33b5c9;
    --teal-shadow: #bfe6ee;
    --paper: #ffffff;
    --paper-edge: #e6f4f8;
    --band-top: #2e9fc4;
    --band-bottom: #2aa3b8;
    --pill: #e9f7fb;
    --gold: #d8a93a;
    --gold-light: #f3d57e;
    --ribbon: #c9332e;
    --highlight: #ffe347;
    --figure: #4b5d7a;
    --figure-top: #3aa6d0;
  }
  * { margin: 0; padding: 0; box-sizing: border-box; }
  html, body { width: 750px; height: 1200px; overflow: hidden; background: var(--paper); }
  .cover {
    position: relative;
    width: 750px; height: 1200px;
    background: var(--paper);
    box-shadow: inset 0 0 0 10px var(--paper-edge);
    font-family: "Noto Sans JP", sans-serif;
    color: var(--ink);
    overflow: hidden;
  }

  /* award badge */
  .award { position: absolute; left: 18px; top: 14px; width: 200px; height: 200px; }
  .award svg { position: absolute; inset: 0; }
  .award-text {
    position: absolute; left: 0; top: 44px; width: 200px;
    text-align: center; color: #5a3d05; font-weight: 900; line-height: 1.05;
  }
  .award-text .small { font-size: 24px; display: block; }
  .award-text .rank { font-size: 44px; display: block; }
  .award-text .count { display: inline-block; margin-top: 12px; font-size: 22px; color: var(--gold-light); }

  /* title */
  .title { font-weight: 900; }
  .title-lead {
    position: absolute; right: 36px; top: 64px;
    writing-mode: vertical-rl;
    font-size: 76px; font-weight: 900; line-height: 1;
  }
  .title-main {
    position: absolute;
    writing-mode: vertical-rl;
    font-family: "M PLUS Rounded 1c", "Noto Sans JP", sans-serif;
    font-weight: 800; font-size: 116px; line-height: 1;
    color: var(--teal);
    text-shadow: 8px 8px 0 var(--teal-shadow);
  }
  .title-main.first { left: 446px; top: 50px; }
  .title-main.second { left: 262px; top: 150px; }

  /* topic chips */
  .topics { position: absolute; left: 22px; top: 300px; list-style: none; }
  .topic {
    width: 170px; height: 56px; margin-bottom: 14px;
    border: 3px solid var(--teal); border-radius: 28px;
    background: var(--paper);
    display: flex; align-items: center; justify-content: center;
    font-weight: 700; font-size: 26px; position: relative;
  }
  .topic::after {
    content: ""; position: absolute; right: 22px; bottom: -11px;
    width: 16px; height: 16px; background: var(--paper);
    border-right: 3px solid var(--teal); border-bottom: 3px solid var(--teal);
    transform: rotate(45deg);
  }

  .figure {
    position: absolute; left: 446px; top: 590px; width: 110px; height: 180px;
    background: linear-gradient(180deg, var(--figure-top) 0%, var(--figure-top) 42%, var(--figure) 43%, var(--figure) 100%);
    border-radius: 50px 50px 14px 14px; opacity: 0.9;
  }

  .byline { position: absolute; left: 210px; top: 784px; display: flex; align-items: center; gap: 24px; }
  .credential { font-size: 20px; font-weight: 700; line-height: 1.35; }
  .author { font-size: 36px; font-weight: 700; letter-spacing: 0.04em; }

  /* bottom band */
  .band {
    position: absolute; left: 0; right: 0; top: 848px; bottom: 0;
    background: linear-gradient(180deg, var(--band-top), var(--band-bottom));
    color: var(--paper);
  }
  .band-row { position: absolute; left: 0; right: 0; display: flex; align-items: center; line-height: 1.2; }
  .lead-big { font-size: 54px; font-weight: 900; line-height: 1.1; }
  .pill { background: var(--paper); color: var(--ink); border-radius: 40px; font-weight: 700; line-height: 1.3; }
  .lead-1 { top: 14px; left: 44px; gap: 22px; }
  .lead-1 .pill { font-size: 26px; padding: 6px 24px; }
  .lead-2 { top: 82px; left: 36px; }
  .lead-2 .lead-big { color: var(--ink); background: var(--paper); padding: 2px 10px; }
  .lead-3 { top: 160px; justify-content: center; }
  .lead-3 .pill { background: var(--pill); font-size: 30px; padding: 6px 46px; }
  .lead-4 { top: 230px; justify-content: center; font-size: 24px; font-weight: 900; }
  .lead-5 { top: 270px; justify-content: center; font-size: 32px; font-weight: 900; }
  .hint { color: var(--highlight); font-size: 48px; margin-right: 6px; }
</style>
</head>
<body>
<main class="cover">

  <div class="award">
    <svg viewBox="0 0 200 200" aria-hidden="true">
      <circle cx="100" cy="100" r="96" fill="var(--gold)"/>
      <circle cx="100" cy="100" r="82" fill="var(--gold-light)"/>
      <rect x="42" y="136" width="116" height="32" fill="var(--ribbon)"/>
    </svg>
    <div class="award-text">
      <span class="small">累計Borelo</span>
      <span class="rank">1位</span>
      <span class="count">59冠</span>
    </div>
  </div>

  <h1 class="title">
    <span class="title-lead">うつむく朝に灯す</span>
    <span class="title-main first">ひと匙の</span>
    <span class="title-main second">言葉</span>
  </h1>

  <ul class="topics">
    <li class="topic">人間関係</li>
    <li class="topic">恋愛</li>
    <li class="topic">仕事</li>
    <li class="topic">お金</li>
    <li class="topic">家族</li>
    <li class="topic">友人</li>
    <li class="topic">自分自身</li>
  </ul>

  <div class="figure" role="img" aria-label="うつむいて肩を落とす人物のイラスト"></div>

  <div class="byline">
    <p class="credential">ウェルネスバランスコーチ<br>検定資格保持者</p>
    <p class="author">○○○○著</p>
  </div>

  <section class="band">
    <div class="band-row lead-1">
      <span class="lead-big">人生には</span>
      <span class="pill">周囲に気付かれない悩みに</span>
    </div>
    <div class="band-row lead-2">
      <span class="lead-big">落ち込むことがいっぱい。</span>
    </div>
    <div class="band-row lead-3">
      <span class="pill">自殺を含む考えが頭をよぎったら</span>
    </div>
    <div class="band-row lead-4">ウェルネスバランスコーチ検定資格保持者が贈る</div>
    <div class="band-row lead-5"><span class="hint">「人生のヒント」</span>をあなたに</div>
  </section>

</main>
</body>
</html>
```